Business Card Design

I am a mental health counselor in private practice. I provide counseling to individuals, couples, and adults. There is a design on CardLoom that I really like. It is 2 talking bubbles joined together by a heart. That is just a suggestion. I'm interested in other ideas. I would like my photo to be on the back of the card, along with the text Miriam Delacott Counseling. I would like mint green as my background color and navy writing, if possible. The final design should be elegant, professional, and maybe just a touch whimsical.
Target Market(s)
Individual adolescents, adults, couples, and families seeking counseling.
Industry/Entity Type
Mental Health
Contact Information for Business Card
Miriam Delacott
A Wholehearted Approach to Counseling
Miriam Delacott, M.S. NCC
Wexmoor Hall
2947 NW Calloway Street, Suite 318
Portland OR 97209
503-286-1573
counselingwithmiriam-example.com
Requirements
Must have
- The card must have all of the text provided and my photo.
Nice to have
- I like cards that are rounded on the sides, and I like thick paper.

```html
<!DOCTYPE html>
<html lang="en">
<head>
<meta charset="utf-8">
<title>Miriam Delacott Counseling – Business Card</title>
<link rel="stylesheet" href="https://fonts.googleapis.com/css2?family=Michroma&family=Questrial&display=swap">
<style>
  :root {
    --lime: #a8f500;
    --lime-deep: #8fd400;
    --ink: #0b0b0b;
    --navy: #0d3568;
    --white: #ffffff;
    --page: #e9e6e1;
    --display: "Michroma", sans-serif;
    --body: "Questrial", sans-serif;
  }
  * { box-sizing: border-box; margin: 0; padding: 0; }
  html, body { width: 1200px; height: 1200px; overflow: hidden; background: var(--page); }
  .sheet { position: relative; width: 1200px; height: 1200px; }

  .card {
    position: absolute; left: 130px; width: 940px; height: 520px;
    border-radius: 34px; overflow: hidden;
    box-shadow: 0 10px 30px rgba(0,0,0,.18);
  }

  /* Front */
  .card--front { top: 50px; background: radial-gradient(ellipse at 40% 55%, var(--lime) 55%, var(--lime-deep) 100%); }
  .front__name-pill {
    position: absolute; left: 0; top: 70px; width: 560px; height: 72px;
    background: var(--ink); border-radius: 0 36px 36px 0;
    display: flex; align-items: center; padding-left: 34px;
  }
  .front__name { font-family: var(--display); font-size: 40px; color: var(--navy); letter-spacing: 1px; white-space: nowrap; }
  .front__tagline {
    position: absolute; left: 70px; top: 158px;
    font-family: var(--body); font-size: 22px; color: var(--navy); letter-spacing: .5px;
  }
  .front__portrait {
    position: absolute; right: 70px; bottom: 0; width: 340px; height: 330px;
    border-radius: 170px 170px 0 0;
    background: radial-gradient(circle at 50% 35%, #f1dcc4 0 22%, #e6d7a8 30%, #2a2a2a 62%, #1a1a1a 100%);
  }

  /* Back */
  .card--back { top: 630px; background: var(--ink); }
  .back__stripe { position: absolute; right: 0; top: 0; width: 170px; height: 100%; background: var(--lime); }
  .back__name-pill {
    position: absolute; left: 0; top: 46px; width: 660px; height: 126px;
    background: var(--lime); border-radius: 0 63px 63px 0;
    padding: 14px 0 0 30px;
  }
  .back__name { font-family: var(--display); font-size: 50px; color: var(--navy); line-height: 1.1; white-space: nowrap; }
  .back__role { font-family: var(--display); font-size: 27px; color: var(--navy); line-height: 1.2; }
  .back__address {
    position: absolute; left: 30px; top: 200px; width: 700px;
    font-family: var(--display); font-variant: small-caps; font-size: 19px;
    color: var(--white); line-height: 1.7; letter-spacing: 2px;
  }
  .back__phone-pill {
    position: absolute; left: 0; top: 300px; width: 560px; height: 80px;
    background: var(--lime); border-radius: 0 40px 40px 0;
    display: flex; align-items: center; padding-left: 30px;
    font-family: var(--display); font-size: 30px; color: var(--navy); letter-spacing: 1px;
  }
  .back__website {
    position: absolute; left: 30px; top: 420px;
    font-family: var(--display); font-size: 26px; color: var(--white); letter-spacing: 1px;
  }
</style>
</head>
<body>
<main class="sheet">
  <section class="card card--front" aria-label="Card front">
    <div class="front__name-pill"><span class="front__name">Miriam Delacott</span></div>
    <p class="front__tagline">A Wholehearted Approach to Counseling Miriam Delacott</p>
    <div class="front__portrait" role="img" aria-label="Portrait photo of Miriam Delacott"></div>
  </section>

  <section class="card card--back" aria-label="Card back">
    <div class="back__stripe"></div>
    <div class="back__name-pill">
      <p class="back__name">Miriam Delacott</p>
      <p class="back__role">mental health counselor</p>
    </div>
    <p class="back__address">M.S. NCC Wexmoor Hall 2947 NW Calloway Street, Suite 318 Portland OR 97209</p>
    <p class="back__phone-pill">Phone : 503-286-1573</p>
    <p class="back__website">counselingwithmiriam-example.com</p>
  </section>
</main>
</body>
</html>
```